Lorn & Vell Designs - Promotions flyer

I am a locally based Interior designer /stylist on Sydney's lower north shore. I would like to offer my services:
Full Professional Styling Services and Furniture Hire
Colour Consultation – Interior / exterior
Floor Coverings
Furniture selection and sourcing
Window Treatments
Wallpaper
Soft Furnishings
Upholstery
Renovations

I would like to offer a free consultation
Updates

Project Deadline Extended
Reason: I've been speaking with a designer and need her to make one more change. I have tried to message her twice, but have had no reply. Once she makes these changes I'm ready to sign off on the design. Thanks Harriet

Target Market(s)

30 - 60's middle to high income earners

Industry/Entity Type

Floor

Requirements
Must have
• one sided DL size
Use my logo
1 or 2 images of interior space or image of a lamp, cushion, lounge etc
The following contact details:
Mobile: 041 xxx xxxx
Website Address: www.lornandvelldesigns.example.au

```html
<!DOCTYPE html>
<html lang="en">
<head>
<meta charset="utf-8">
<title>Lorn &amp; Vell Designs – Promotions Flyer</title>
<link rel="stylesheet" href="https://fonts.googleapis.com/css2?family=Oswald:wght@500&family=Questrial&display=swap">
<style>
  :root {
    --orange: #ee7a22;
    --white: #ffffff;
    --taupe: #d2c9b6;
    --ink: #1a1a1a;
    --photo-light: #c9c9c9;
    --photo-mid: #8d8e94;
    --photo-dark: #3a3b42;
  }
  * { box-sizing: border-box; margin: 0; padding: 0; }
  html, body { width: 1200px; height: 566px; overflow: hidden; background: var(--white); }
  .flyer {
    position: relative;
    width: 1200px;
    height: 566px;
    font-family: "Questrial", Arial, sans-serif;
  }
  .brand-panel {
    position: absolute; left: 0; top: 0;
    width: 356px; height: 140px;
    background: var(--white);
    display: flex; align-items: center; justify-content: center;
  }
  .brand-name {
    font-family: "Questrial", Arial, sans-serif;
    font-size: 32px;
    color: var(--ink);
    line-height: 1;
  }
  .services-panel {
    position: absolute; left: 0; top: 140px;
    width: 356px; height: 346px;
    background: var(--orange);
    color: var(--white);
    padding: 58px 19px 0;
    font-size: 13.3px;
    line-height: 14.6px;
  }
  .services-intro { margin-bottom: 15px; }
  .services-list { list-style: none; }
  .free-offer { position: absolute; left: 19px; top: 282px; }
  .contact-panel {
    position: absolute; left: 0; top: 486px;
    width: 356px; height: 80px;
    background: var(--white);
    color: var(--ink);
    padding: 25px 20px 0;
    font-size: 13px;
    line-height: 15px;
  }
  .feature-panel {
    position: absolute; left: 356px; top: 0;
    width: 844px; height: 566px;
    background: var(--taupe);
  }
  .feature-photo {
    position: absolute; left: 56px; top: 0;
    width: 733px; height: 486px;
    background: linear-gradient(160deg, var(--photo-light) 0%, #dcdcdc 35%, var(--photo-mid) 65%, var(--photo-dark) 100%);
  }
  .tagline {
    position: absolute; left: 0; top: 514px;
    width: 844px;
    text-align: center;
    font-family: "Oswald", "Arial Narrow", sans-serif;
    font-weight: 500;
    font-size: 22px;
    letter-spacing: 0.2px;
    color: var(--white);
  }
</style>
</head>
<body>
  <main class="flyer">
    <header class="brand-panel">
      <span class="brand-name">Lorn &amp; Vell Designs</span>
    </header>

    <section class="services-panel">
      <p class="services-intro">At Lorn &amp; Vell Designs we offer:</p>
      <ul class="services-list">
        <li>Full Professional Styling Services and Furniture Hire</li>
        <li>Colour Consultation – Interior / exterior</li>
        <li>Floor Coverings</li>
        <li>Furniture selection and sourcing</li>
        <li>Window Treatments</li>
        <li>Wallpaper</li>
        <li>Soft Furnishings</li>
        <li>Upholstery</li>
        <li>Renovations</li>
      </ul>
      <p class="free-offer">Free consultation</p>
    </section>

    <footer class="contact-panel">
      <p>Mobile: 041 xxx xxxx</p>
      <p>Web: www.lornandvelldesigns.example.au</p>
    </footer>

    <section class="feature-panel">
      <div class="feature-photo" role="img" aria-label="Styled bedroom with a carved white headboard, white pillows, silver buttoned cushions, a grey quilted bedspread, a patterned lamp and an ornate silver mirror"></div>
      <p class="tagline">TRANSFORMING LIVING SPACES WITH LORN &amp; VELL DESIGNS!</p>
    </section>
  </main>
</body>
</html>
```